6 Banners for $150,000 Media Campaign in Sydney

Please design a series of call to action banners to advertise this campaign and encourage people to join the CHIROPRACTIC CAMPAIGN

https://www.fundorvale.example/projects/sydney-spinewell-drive-2015

banner must rotate with 3 screens and not be longer than 30 seconds in total and less than 45kb

The call to action must be "Join The Campaign"

These are the sizes:
160x600.gif
728x90.gif
300x250.gif
320x50.gif
300x600.gif

600x315.jpeg (and text can only be 20% of image area - https://www.plimora.example/ads/tools/text_overlay)

FRAME 1:
12 WEEK Chiropractic Campaign (Sydney)
Start June 2015

FRAME 2:
"KEEP YOUR BACK HAPPY"

FRAME 3:
Strictly limited to 300 members

CALL TO ACTION:
JOIN NOW

Target Market(s)

business owners: chiropractors

Industry/Entity Type

Media

Font styles to use
Sans Serif

Requirements
Must have
• strong call to action
• please present ALL banners in a SINGLE file / image

```html
<!DOCTYPE html>
<html lang="en">
<head>
<meta charset="utf-8">
<title>12 Week Chiropractic Campaign (Sydney) – Banner Set</title>
<link rel="stylesheet" href="https://fonts.googleapis.com/css2?family=Fjalla+One&display=swap">
<style>
  :root {
    --campaign-blue: #10a6e4;
    --corner-black: #050505;
    --headline-ink: #0b0b0b;
    --label-white: #ffffff;
    --spine-deep: #0b4f8f;
    --spine-glow: #5cc8ff;
    --spine-hot: #ff2f6d;
    --page: #ffffff;
  }
  html, body {
    margin: 0;
    padding: 0;
    width: 1200px;
    height: 1062px;
    overflow: hidden;
    background: var(--page);
  }
  .banner-set {
    position: relative;
    width: 1200px;
    height: 1062px;
    font-family: "Fjalla One", "Arial Narrow", sans-serif;
  }
  .banner {
    position: absolute;
    overflow: hidden;
    background: var(--campaign-blue);
    color: var(--headline-ink);
  }
  .corner {
    position: absolute;
    left: 0;
    top: 0;
  }
  .corner polygon { fill: var(--corner-black); }
  .start-label {
    position: absolute;
    color: var(--label-white);
    white-space: nowrap;
    transform: translate(-50%, -50%) rotate(-45deg);
    line-height: 1;
  }
  .headline {
    position: absolute;
    margin: 0;
    font-weight: 400;
    text-align: center;
    line-height: 1.24;
    letter-spacing: 0.5px;
  }
  .spine-art {
    position: absolute;
    background:
      radial-gradient(ellipse 14% 16% at 50% 68%, var(--spine-hot) 0%, rgba(255,47,109,0) 100%),
      radial-gradient(ellipse 45% 60% at 50% 55%, var(--spine-glow) 0%, var(--spine-deep) 70%, rgba(11,79,143,0) 100%);
  }

  /* 160x600 skyscraper */
  .banner--skyscraper { left: 4px; top: 12px; width: 232px; height: 868px; }
  .banner--skyscraper .start-label { left: 78px; top: 78px; font-size: 25px; }
  .banner--skyscraper .headline { left: 0; right: 0; top: 300px; font-size: 40px; }
  .banner--skyscraper .spine-art { left: 0; top: 568px; width: 232px; height: 300px; }

  /* 300x250 medium rectangle */
  .banner--rectangle { left: 278px; top: 12px; width: 435px; height: 362px; }
  .banner--rectangle .start-label { left: 64px; top: 64px; font-size: 23px; }
  .banner--rectangle .headline { left: 110px; width: 250px; top: 74px; font-size: 38px; line-height: 1.3; }
  .banner--rectangle .spine-art { left: 302px; top: 191px; width: 116px; height: 171px; }

  /* 320x50 mobile */
  .banner--mobile { left: 264px; top: 428px; width: 464px; height: 72px; }
  .banner--mobile .start-label { left: 25px; top: 25px; font-size: 9px; }
  .banner--mobile .headline { left: 48px; width: 330px; top: 0; line-height: 72px; font-size: 16px; }
  .banner--mobile .spine-art { left: 396px; top: 0; width: 58px; height: 72px; }

  /* 300x600 half page */
  .banner--halfpage { left: 755px; top: 12px; width: 435px; height: 868px; }
  .banner--halfpage .start-label { left: 140px; top: 140px; font-size: 45px; }
  .banner--halfpage .headline { left: 20px; right: 20px; top: 392px; font-size: 42px; }
  .banner--halfpage .spine-art { left: 187px; top: 605px; width: 218px; height: 263px; }

  /* 728x90 leaderboard */
  .banner--leaderboard { left: 135px; top: 915px; width: 1056px; height: 130px; }
  .banner--leaderboard .start-label { left: 44px; top: 44px; font-size: 14px; }
  .banner--leaderboard .headline { left: 140px; width: 730px; top: 0; line-height: 130px; font-size: 38px; }
  .banner--leaderboard .spine-art { left: 938px; top: 0; width: 94px; height: 130px; }
</style>
</head>
<body>
<main class="banner-set">

  <section class="banner banner--skyscraper" aria-label="160 by 600 banner">
    <svg class="corner" width="232" height="232" viewBox="0 0 232 232"><polygon points="0,0 232,0 0,228"/></svg>
    <span class="start-label">Start June 2015</span>
    <h2 class="headline">12 WEEK<br>Chiropractic<br>Campaign<br>(Sydney)</h2>
    <div class="spine-art" role="img" aria-label="Glowing blue x-ray figure of a human skeleton with the lower spine highlighted in red"></div>
  </section>

  <section class="banner banner--rectangle" aria-label="300 by 250 banner">
    <svg class="corner" width="180" height="180" viewBox="0 0 180 180"><polygon points="0,0 178,0 0,178"/></svg>
    <span class="start-label">Start June 2015</span>
    <h2 class="headline">12 WEEK<br>Chiropractic<br>Campaign<br>(Sydney)</h2>
    <div class="spine-art" role="img" aria-label="Glowing blue x-ray figure of a human skeleton with the lower spine highlighted in red"></div>
  </section>

  <section class="banner banner--mobile" aria-label="320 by 50 banner">
    <svg class="corner" width="76" height="72" viewBox="0 0 76 72"><polygon points="0,0 76,0 0,72"/></svg>
    <span class="start-label">Start June 2015</span>
    <h2 class="headline">12 WEEK Chiropractic Campaign (Sydney)</h2>
    <div class="spine-art" role="img" aria-label="Glowing blue x-ray figure of a human skeleton with the lower spine highlighted in red"></div>
  </section>

  <section class="banner banner--halfpage" aria-label="300 by 600 banner">
    <svg class="corner" width="405" height="410" viewBox="0 0 405 410"><polygon points="0,0 405,0 0,410"/></svg>
    <span class="start-label">Start June 2015</span>
    <h2 class="headline">12 WEEK Chiropractic<br>Campaign<br>(Sydney)</h2>
    <div class="spine-art" role="img" aria-label="Glowing blue x-ray figure of a human skeleton with the lower spine highlighted in red"></div>
  </section>

  <section class="banner banner--leaderboard" aria-label="728 by 90 banner">
    <svg class="corner" width="134" height="130" viewBox="0 0 134 130"><polygon points="0,0 134,0 0,130"/></svg>
    <span class="start-label">Start June 2015</span>
    <h2 class="headline">12 WEEK Chiropractic Campaign (Sydney)</h2>
    <div class="spine-art" role="img" aria-label="Glowing blue x-ray figure of a human skeleton with the lower spine highlighted in red"></div>
  </section>

</main>
</body>
</html>
```